Digital & Print Graphic Design templates for Comedy Club

We need new new digital & print graphic design templates for our upcoming comedy events created for use in CANVA in the following specs
Digital:
1080x1080px
1200x600px
800x400px
1920x1080px
1080x1355px
1500x500px
851x315px
Print
11x17"
22x28"
95.5x30"

Target Market(s)

18+ comedy fans

Industry/Entity Type

comedy club

Font styles to use
Sans Serif

Colors
FFF300
FFF600
FEFA6F
FFFEC7
FFFEE8
6B429C
8869AF
B7A5CE
E3DAEB
F3F0F8

Requirements
Must have
• templates must be CANVA compatible. frame for comedian photo.
Nice to have
• would like to incorporate deep purple into the design
Should not have
• do not include phone number on any templates

```html
<!DOCTYPE html>
<html lang="en">
<head>
<meta charset="utf-8">
<title>Chuckle Cellar – Event Templates</title>
<link href="https://fonts.googleapis.com/css2?family=Alfa+Slab+One&display=swap" rel="stylesheet">
<style>
  :root {
    --yellow: #FFF300;
    --purple-deep: #43337E;
    --purple-card: #5445A8;
    --purple-dark: #3A2A86;
    --beam: rgba(190, 180, 90, 0.45);
    --shadow: rgba(20, 16, 40, 0.85);
    --white: #FFFFFF;
  }
  html, body {
    margin: 0;
    padding: 0;
    width: 1200px;
    height: 1200px;
    overflow: hidden;
  }
  .board {
    position: relative;
    width: 1200px;
    height: 1200px;
    background: var(--yellow);
    overflow: hidden;
  }
  .board__bands {
    position: absolute;
    inset: 0;
  }
  .template {
    position: absolute;
    background: var(--purple-card);
    box-shadow: 10px 10px 6px var(--shadow);
    overflow: hidden;
  }
  .template--landscape { left: 64px; top: 228px; width: 562px; height: 314px; }
  .template--portrait  { left: 710px; top: 104px; width: 362px; height: 560px; }
  .template--square    { left: 144px; top: 666px; width: 402px; height: 404px; }
  .template__art {
    position: absolute;
    inset: 0;
  }
  .club-mark {
    position: absolute;
    display: flex;
    align-items: center;
    justify-content: center;
    border-radius: 50%;
  }
  .club-mark__glow {
    position: absolute;
    inset: -22px;
    border-radius: 50%;
    background: radial-gradient(circle, rgba(255,243,0,0.9) 55%, rgba(255,243,0,0) 72%);
  }
  .club-mark__disc {
    position: absolute;
    inset: 0;
    border-radius: 50%;
    background: var(--purple-dark);
    border: 2px solid var(--white);
  }
  .club-mark__name {
    position: relative;
    font-family: "Alfa Slab One", serif;
    color: var(--yellow);
    text-align: center;
    line-height: 1.05;
    text-transform: uppercase;
  }
  .template--landscape .club-mark { left: 173px; top: 46px; width: 226px; height: 226px; }
  .template--landscape .club-mark__name { font-size: 34px; }
  .template--portrait .club-mark { left: 80px; top: 185px; width: 212px; height: 212px; }
  .template--portrait .club-mark__name { font-size: 32px; }
  .template--square .club-mark { left: 38px; top: 220px; width: 168px; height: 168px; }
  .template--square .club-mark__name { font-size: 24px; }
  .comedian-photo {
    position: absolute;
    left: 180px;
    top: 122px;
    width: 222px;
    height: 282px;
    background: linear-gradient(160deg, #F4F2F0 0%, #D9CFC6 55%, #3A3434 100%);
  }
  .headliner {
    position: absolute;
    left: 22px;
    top: 72px;
    margin: 0;
    font-family: "Alfa Slab One", serif;
    font-weight: 400;
    font-size: 40px;
    letter-spacing: 1px;
    color: var(--yellow);
    transform: rotate(-4deg);
    transform-origin: left center;
    white-space: nowrap;
  }
</style>
</head>
<body>
<main class="board">
  <svg class="board__bands" width="1200" height="1200" viewBox="0 0 1200 1200" aria-hidden="true">
    <polygon points="0,0 1200,0 1200,22 552,104 608,60 0,136" fill="var(--purple-deep)"/>
    <polygon points="0,1152 1136,1064 840,1040 1200,896 1200,1200 0,1200" fill="var(--purple-deep)"/>
  </svg>

  <section class="template template--landscape">
    <svg class="template__art" width="562" height="314" viewBox="0 0 562 314" aria-hidden="true">
      <polygon points="0,0 128,0 240,260 0,80" fill="var(--beam)"/>
      <polygon points="420,0 562,0 562,80 320,260" fill="var(--beam)"/>
    </svg>
    <div class="club-mark">
      <div class="club-mark__glow" role="img" aria-label="Yellow paint splash behind the club name"></div>
      <div class="club-mark__disc"></div>
      <span class="club-mark__name">Chuckle<br>Cellar</span>
    </div>
  </section>

  <section class="template template--portrait">
    <svg class="template__art" width="362" height="560" viewBox="0 0 362 560" aria-hidden="true">
      <polygon points="0,0 120,0 190,0 150,230 0,60" fill="var(--beam)"/>
      <polygon points="150,0 362,0 362,60 210,230" fill="var(--beam)"/>
    </svg>
    <div class="club-mark">
      <div class="club-mark__glow" role="img" aria-label="Yellow paint splash behind the club name"></div>
      <div class="club-mark__disc"></div>
      <span class="club-mark__name">Chuckle<br>Cellar</span>
    </div>
  </section>

  <section class="template template--square">
    <div class="comedian-photo" role="img" aria-label="Comedian headshot photo frame"></div>
    <svg class="template__art" width="402" height="404" viewBox="0 0 402 404" aria-hidden="true">
      <polygon points="0,70 402,28 402,110 0,150" fill="var(--purple-dark)"/>
      <polygon points="0,150 180,132 0,164" fill="#111"/>
      <polygon points="90,40 402,8 402,18" fill="#111"/>
    </svg>
    <h2 class="headliner">MAX RUDLEY</h2>
    <div class="club-mark">
      <div class="club-mark__glow" role="img" aria-label="Yellow paint splash behind the club name"></div>
      <div class="club-mark__disc"></div>
      <span class="club-mark__name">Chuckle<br>Cellar</span>
    </div>
  </section>
</main>
</body>
</html>
```